Book Cover (HALF OF ALL WORRIES FADE AWAY)

This book is a series of blog posts from my blog, Notes Fit for Borrowing, which is at glenmarwick.com/blog.
The book is to be called:
HALF OF ALL WORRIES FADE AWAY
And 51 other Notes Fit for Borrowing from the Small Business Sage
(Notes Fit for Borrowing) should be italicized.
My name is Glen Marwick, M.B.A.

I will need three variations for my paperback, hardcover and e-book.
Here are some of the blog titles and their topics:
Preparing Your Small Business For Recession small business recession
Should I Incorporate My Business? Should I Incorporate My Business?
Alternative to Minority Shareholder In Small Private Companies minority shareholder
Small Business Culture – Getting it Right Small Business Culture
What is The Right Way to Fire Someone The Right Way to Fire Someone
The Five Basic Leadership Principles Leadership Principles
10 Tips for New Entrepreneurs – Sure Ways to Increase Your Chances of Success
10 things to consider before becoming an entrepreneur
Strategy vs Biz Plans small business strategy
Closing Sales close the sale
Breakeven break even
Growth makes cash flow suck cash flow issues
Think Twice About Offering Early Payment Discounts prepayment discounts
Firing Customers firing customers
Collections best practices getting paid faster
The Cash Flow Statement cash flow statement
Using Paralegals paralegal
Radical Candor radical candor
Why No is the Second Best Word to a Salesperson's ears value of no
The $8 Million Problem -
Contractor vs Employee contractor vs employee
The Vantrell sales tactic
Systems Turn Goals From Dreams Into Reality Systems vs Goals
The Importance of Realistic Goals stretch goals
Why The Owner Must Review Every Hire hiring for values
Systems Thinking for Small Biz: The Case for SOPs systems thinking
Trust Your Gut business intuition
Grease and friction grease vs friction
Left alone, 90% of problems solve themselves strategic inaction
Referrals Are Great—But Not a Growth Strategy referrals
The Lean Marketing Machine: 7 Hacks to Grow Your Small Business Fast marketing hacks
The Small Business Health Check small business health check
How to Spot a Customer Headed for Trouble — Before They Take You Down With Them customer warning signs
We Are What We Repeatedly Do habits
The Smartest People Know When to Play Dumb playing dumb
Before You Scale, Do the Math unit economics
AI for Small Business: Practical Tools and Use Cases AI for Small Business
Title: Tell Me Right Now—Why Can’t We Raise Your Prices? small business pricing
Why Your Real Competitor Isn’t Who You Think creative destruction
Good Enough Might Be Great satisficing
Bootstrapping: Building Your Business on Your Terms bootstrapping
Building Resilient Companies That Never Have to Bet the Farm bet the farm
We Always Overshoot: From Fiber to Cannabis to AI AI overbuild
A Bias Toward Action bias toward ation
Choosing the Right Business Owner Title business owner title
Jobs to Be Done: Understanding What Your Customers Really Want Jobs to Be Done
Forget Money. Here’s What Really Motivates People. motivation

Target Market(s)

Small business operators, business school students

Industry/Entity Type

Small business

Colors

Designer to choose colors to be used in the design.

Requirements
Should not have
• Should not look cartoonish

```html
<!DOCTYPE html>
<html lang="en">
<head>
<meta charset="utf-8">
<title>Half of All Worries Fade Away — Glen Marwick, M.B.A.</title>
<link rel="stylesheet" href="https://fonts.googleapis.com/css2?family=Righteous&family=Lexend:wght@400;500&display=swap">
<style>
  :root {
    --paper: #fefdf3;
    --coral: #f26c55;
    --slate: #86a1a1;
    --slate-deep: #6e8c8c;
  }
  html, body {
    margin: 0;
    padding: 0;
    overflow: hidden;
    background: var(--paper);
  }
  .cover {
    position: relative;
    width: 800px;
    height: 1200px;
    overflow: hidden;
    background: var(--paper);
    font-family: "Righteous", "Arial", sans-serif;
  }
  .cover-art {
    position: absolute;
    left: 74px;
    top: 104px;
    width: 480px;
    height: 632px;
  }
  .title {
    position: absolute;
    left: 76px;
    top: 744px;
    margin: 0;
    font-weight: 400;
    font-size: 92px;
    line-height: 81px;
    letter-spacing: 0;
    white-space: nowrap;
  }
  .title-line { display: block; }
  .title-line--accent { color: var(--coral); }
  .title-line--muted { color: var(--slate); }
  .rule {
    position: absolute;
    left: 0;
    top: 1008px;
    width: 800px;
    height: 2px;
    background: var(--coral);
  }
  .author {
    position: absolute;
    right: 107px;
    top: 1026px;
    margin: 0;
    font-size: 30px;
    line-height: 36px;
    color: var(--slate);
    white-space: nowrap;
  }
  .author-credential {
    font-size: 20px;
  }
  .subtitle {
    position: absolute;
    left: 78px;
    top: 1086px;
    width: 615px;
    margin: 0;
    font-family: "Lexend", "Arial", sans-serif;
    font-weight: 400;
    font-size: 18px;
    line-height: 26px;
    color: var(--slate-deep);
  }
  .subtitle em {
    font-style: italic;
    color: var(--coral);
  }
</style>
</head>
<body>
  <main class="cover">
    <svg class="cover-art" viewBox="0 0 480 632" role="img"
         aria-label="Illustration of a coiled rattlesnake shaking its tail, red lightning marks above it, with a faded reflection below">
      <defs>
        <linearGradient id="art-tone" x1="0" y1="0" x2="0" y2="1">
          <stop offset="0" stop-color="#f4a08f"/>
          <stop offset="0.3" stop-color="#c9d6d8"/>
          <stop offset="0.62" stop-color="#7f9c9c"/>
          <stop offset="0.72" stop-color="#d5e0e4"/>
          <stop offset="1" stop-color="#eef2f2"/>
        </linearGradient>
      </defs>
      <rect width="480" height="632" rx="24" fill="url(#art-tone)"/>
    </svg>

    <h1 class="title">
      <span class="title-line title-line--accent">HALF OF ALL</span>
      <span class="title-line title-line--accent">WORRIES</span>
      <span class="title-line title-line--muted">FADE AWAY</span>
    </h1>

    <div class="rule"></div>

    <p class="author">GLEN MARWICK<span class="author-credential">, M.B.A.</span></p>

    <p class="subtitle">And 51 other <em>Notes Fit for Borrowing</em><br>from the Small Business Sage</p>
  </main>
</body>
</html>
```